Verdant Harvest Collective - Business Card Design Project

We need business cards for our business. We grow roots and fruits in Central and South America, we import and distribute in FL, USA. We do fresh and frozen products.

Target Market(s)

Small and big supermarkets, wholesalers, traders, distributors, etc

Industry/Entity Type

Business

```html
<!DOCTYPE html>
<html lang="en">
<head>
<meta charset="utf-8">
<title>Verdant Harvest Collective – Business Cards</title>
<link href="https://fonts.googleapis.com/css2?family=Roboto+Condensed:wght@400;500&display=swap" rel="stylesheet">
<style>
  :root {
    --backdrop-top: #a9acaa;
    --backdrop-bottom: #c9cac9;
    --card-white: #ffffff;
    --card-mist: #eef0ee;
    --harvest-orange: #ec8a28;
    --orange-light: #f4a457;
    --forest-green: #4f6231;
    --leaf-green: #5c7035;
    --olive-green: #9ca22f;
    --ink: #1f1f1f;
  }
  * { margin: 0; padding: 0; box-sizing: border-box; }
  html, body {
    width: 1200px;
    height: 720px;
    overflow: hidden;
  }
  body {
    background: linear-gradient(180deg, var(--backdrop-top), var(--backdrop-bottom));
    font-family: "Roboto Condensed", "Arial Narrow", sans-serif;
    display: flex;
    flex-direction: column;
    align-items: center;
    justify-content: center;
    gap: 40px;
  }
  .card {
    position: relative;
    width: 540px;
    height: 308px;
    overflow: hidden;
    box-shadow: 0 2px 6px rgba(0,0,0,0.18);
  }
  .card--front {
    background: radial-gradient(ellipse at 50% 55%, var(--card-white) 40%, var(--card-mist) 100%);
    border: 1px solid #8a8d8a;
  }
  .card--back { background: var(--harvest-orange); }

  .top-rules {
    position: absolute;
    left: 0; right: 56px; top: 18px;
  }
  .top-rules span {
    display: block;
    height: 4px;
    background: var(--forest-green);
    margin-bottom: 7px;
  }
  .corner-leaf {
    position: absolute;
    right: 8px; top: 4px;
    width: 52px; height: 52px;
    background: var(--leaf-green);
  }
  .world-map {
    position: absolute;
    right: 0; top: 0;
    width: 330px; height: 100%;
    background: linear-gradient(160deg, var(--orange-light) 0%, #f09a48 55%, var(--harvest-orange) 100%);
    opacity: 0.75;
  }

  .identity {
    position: absolute;
    left: 0; right: 0;
    text-align: center;
  }
  .card--front .identity { top: 126px; }
  .card--back .identity { top: 80px; }
  .brand-name {
    font-weight: 500;
    font-size: 33px;
    letter-spacing: 1px;
    text-transform: uppercase;
    line-height: 1.1;
  }
  .card--front .brand-name { color: var(--forest-green); }
  .card--back .brand-name { color: var(--card-white); }
  .tagline {
    margin-top: 50px;
    font-size: 13px;
    line-height: 1.35;
    color: var(--ink);
  }
  .swoosh {
    position: absolute;
    left: 0; top: 0;
    width: 540px; height: 308px;
  }
</style>
</head>
<body>
  <section class="card card--front">
    <div class="top-rules"><span></span><span></span></div>
    <div class="corner-leaf" role="img" aria-label="Green leaf illustration in the top corner"></div>
    <div class="identity">
      <p class="brand-name">Verdant Harvest Collective</p>
      <p class="tagline">Small and big supermarkets, wholesalers<br>traders, distributors, etc</p>
    </div>
  </section>

  <section class="card card--back">
    <div class="world-map" role="img" aria-label="Faint world map of the Americas with a hexagon pattern"></div>
    <div class="identity">
      <p class="brand-name">Verdant Harvest Collective</p>
      <p class="tagline">Small and big supermarkets, wholesalers<br>traders, distributors, etc</p>
    </div>
    <svg class="swoosh" viewBox="0 0 540 308" aria-hidden="true">
      <path d="M0,180 C130,182 250,230 320,308 L0,308 Z" fill="var(--card-white)"/>
      <path d="M0,186 C125,188 240,234 307,308 L0,308 Z" fill="var(--olive-green)"/>
      <path d="M0,212 C110,214 210,250 262,308 L0,308 Z" fill="var(--card-white)"/>
      <path d="M0,216 C108,218 206,253 256,308 L0,308 Z" fill="var(--forest-green)"/>
      <path d="M0,244 C80,246 150,270 182,308 L0,308 Z" fill="var(--card-white)"/>
    </svg>
  </section>
</body>
</html>
```